BUSINESS CARD - HALLORAN FIELD SERVICES

I would like to create a business card for my fertilizer spreading business. I would like to incorporate my existing logo and also a description of the services offered. The business card will be given to farmers so must be kept simple but effective. It will also be left in stores so much also be eye catching in order to stand out from other cards.

Target Market(s)

FARMERS

Requirements
Must have
• FRONT OF CARD = EXISTING LOGO + "CUSTOMISED SPREADING" below the logo

REAR Of CARD = SERVICES OFFERED AND CONTACT DETAILS

- Bulk fertilizer including Lime, Gypsum, Manure & Compost
- Granular fertilizer including Single Super, Urea, Gran-am, & Custom Blends
- Modern equipment - Autosteer & Variable Rate Capable
- Friendly & Reliable Service
- Contact Gus: 0471 592 318
Nice to have
• utilize same color scheme as existing logo

```html
<!DOCTYPE html>
<html lang="en">
<head>
<meta charset="utf-8">
<title>Halloran Field Services – Business Card</title>
<link href="https://fonts.googleapis.com/css2?family=Barlow:wght@500;600;700&display=swap" rel="stylesheet">
<style>
  :root {
    --orange: #f59121;
    --orange-light: #f7a744;
    --grey: #5a5a5c;
    --white: #ffffff;
    --backdrop: #2b2b2b;
  }
  * { box-sizing: border-box; margin: 0; padding: 0; }
  html, body { width: 1200px; height: 900px; overflow: hidden; }
  body {
    background: var(--backdrop);
    font-family: "Barlow", Arial, sans-serif;
    position: relative;
  }
  .card {
    position: absolute;
    left: 260px;
    width: 680px;
    height: 388px;
    background: var(--white);
    overflow: hidden;
    box-shadow: 0 10px 30px rgba(0,0,0,.45);
  }
  .card--front { top: 42px; }
  .card--back { top: 470px; }
  .card__shapes { position: absolute; inset: 0; width: 100%; height: 100%; }

  /* brand block */
  .brand { position: absolute; display: flex; align-items: center; gap: 14px; }
  .brand__dot {
    flex: none;
    border-radius: 50%;
    border: 6px solid var(--grey);
  }
  .brand__name {
    color: var(--grey);
    font-weight: 700;
    line-height: 1;
    letter-spacing: -0.5px;
  }
  .card--front .brand { left: 360px; top: 110px; }
  .card--front .brand__dot { width: 78px; height: 78px; }
  .card--front .brand__name { font-size: 32px; }
  .card--back .brand { left: 430px; top: 34px; }
  .card--back .brand__dot { width: 56px; height: 56px; border-width: 5px; }
  .card--back .brand__name { font-size: 23px; }

  .tagline {
    position: absolute;
    left: 400px;
    top: 322px;
    width: 260px;
    height: 22px;
    line-height: 22px;
    text-align: center;
    color: var(--grey);
    font-weight: 600;
    font-size: 17px;
    letter-spacing: 0.5px;
  }

  /* services */
  .services {
    position: absolute;
    left: 36px;
    top: 112px;
    list-style: none;
    color: var(--grey);
    font-size: 15px;
    font-weight: 500;
    line-height: 22px;
  }
  .services__item { position: relative; padding-left: 26px; }
  .services__item--sub { padding-left: 46px; }
  .services__item--sub::before { content: "-"; position: absolute; left: 28px; }
  .services__tick { position: absolute; left: 0; top: 6px; width: 18px; height: 11px; }

  .contact { position: absolute; left: 70px; top: 288px; }
  .contact__name { color: var(--orange); font-size: 28px; font-weight: 700; letter-spacing: 1px; }
  .contact__phone { color: var(--grey); font-size: 34px; font-weight: 700; letter-spacing: 1px; line-height: 1.1; }
</style>
</head>
<body>

<section class="card card--front" aria-label="Card front">
  <svg class="card__shapes" viewBox="0 0 680 388" aria-hidden="true">
    <polygon points="0,0 460,0 224,187 440,340 470,388 0,388" fill="var(--orange)"/>
    <polygon points="0,0 460,0 224,187" fill="var(--orange-light)"/>
    <rect x="0" y="320" width="680" height="26" fill="var(--orange-light)"/>
  </svg>
  <div class="brand">
    <span class="brand__dot"></span>
    <span class="brand__name">HALLORAN FIELD<br>SERVICES</span>
  </div>
  <p class="tagline">CUSTOMISED SPREADING</p>
</section>

<section class="card card--back" aria-label="Card back">
  <svg class="card__shapes" viewBox="0 0 680 388" aria-hidden="true">
    <polygon points="300,0 680,0 680,205 500,165" fill="var(--orange)"/>
    <polygon points="500,165 680,205 680,388 420,388" fill="var(--orange-light)"/>
  </svg>
  <div class="brand">
    <span class="brand__dot"></span>
    <span class="brand__name">HALLORAN FIELD<br>SERVICES</span>
  </div>

  <ul class="services">
    <li class="services__item"><svg class="services__tick" viewBox="0 0 18 11"><path d="M1 5 L7 10 L17 1" fill="none" stroke="var(--orange)" stroke-width="3"/></svg>Bulk Fertilizer including</li>
    <li class="services__item services__item--sub">Lime, Gypsum, Manure &amp; Composts.</li>
    <li class="services__item"><svg class="services__tick" viewBox="0 0 18 11"><path d="M1 5 L7 10 L17 1" fill="none" stroke="var(--orange)" stroke-width="3"/></svg>Granular Fertilizer including</li>
    <li class="services__item services__item--sub">Single Super, Urea, Gran-am, &amp; Custom Blends.</li>
    <li class="services__item"><svg class="services__tick" viewBox="0 0 18 11"><path d="M1 5 L7 10 L17 1" fill="none" stroke="var(--orange)" stroke-width="3"/></svg>Modern Equipments.</li>
    <li class="services__item"><svg class="services__tick" viewBox="0 0 18 11"><path d="M1 5 L7 10 L17 1" fill="none" stroke="var(--orange)" stroke-width="3"/></svg>Friendly &amp; Reliable Service.</li>
  </ul>

  <div class="contact">
    <p class="contact__name">GUS</p>
    <p class="contact__phone">0471 592 318</p>
  </div>
</section>

</body>
</html>
```